PLIVET Buck Slip: Request for Donations to our Program's Development Fund

We would like to create an invitation card/double sided pamplet (about 4x9 inches) to place in orthopaedics clinics and hand/mail out to potential donors about our research program, Westmere Study Group for Joint & Muscle Health. We have attached a copy of a design we've been working with but are looking for more of a professional touch.

Target Market(s)

Patients, Donors

Industry/Entity Type

Medical And Science

Font styles to use
Other font styles liked:
• Gothan Bold, Gotham Book, Gothan, Georgia, Serif, Sans Serif

Colors
ec1f27
f78f20
ffffff
000000
333333
5c5c5c
fbed22
fbee3d
ffc214

Requirements
Must have
• Please use the visual identity standards for guidance to help with colour choice and font selection (https://www.norvalenu.example/brand/system/files/1.0-logo-visual-identity_april2017.pdf)

```html
<!DOCTYPE html>
<html lang="en">
<head>
<meta charset="utf-8">
<title>PLIVET Buck Slip</title>
<link href="https://fonts.googleapis.com/css2?family=Montserrat:ital,wght@0,400;0,500;0,600;0,700;1,400&display=swap" rel="stylesheet">
<style>
  :root {
    --red: #ec1f27;
    --orange: #f78f20;
    --yellow: #ffc214;
    --band-yellow: #fdd00c;
    --white: #ffffff;
    --black: #000000;
    --ink: #333333;
    --grey: #5c5c5c;
    --backdrop: #9c9a9b;
  }
  * { box-sizing: border-box; margin: 0; padding: 0; }
  html, body { width: 1200px; height: 1200px; overflow: hidden; }
  body {
    background: var(--backdrop);
    font-family: "Montserrat", sans-serif;
    color: var(--black);
    position: relative;
  }
  .slip {
    position: absolute;
    left: 88px;
    width: 1022px;
    height: 472px;
    overflow: hidden;
    background: var(--white);
  }
  .slip--front { top: 96px; }
  .slip--back { top: 630px; }

  /* front */
  .hero-photo {
    position: absolute; inset: 0;
    background:
      radial-gradient(ellipse 34% 44% at 70% 58%, #3a2a22 0%, #6b4a3c 30%, rgba(200,150,130,0.85) 55%, rgba(200,160,145,0) 80%),
      linear-gradient(100deg, #f4f5f7 0%, #e8ebef 38%, #cdd3db 60%, #8e9cae 100%);
  }
  .accent-rule {
    position: absolute; left: 0; right: 0; height: 4px;
    background: linear-gradient(90deg, var(--yellow), var(--orange) 70%, var(--red));
  }
  .accent-rule--top { top: 24px; }
  .accent-rule--bottom { top: 447px; }
  .quote {
    position: absolute; left: 26px; top: 222px; width: 460px;
    font-style: italic; font-size: 25px; line-height: 31px;
    color: var(--ink);
  }
  .quote__author {
    position: absolute; left: 26px; top: 380px; width: 444px;
    text-align: right; font-style: italic; font-size: 28px; color: var(--ink);
  }
  .brand-lockup {
    position: absolute; display: flex; align-items: center;
  }
  .brand-lockup--light { left: 594px; top: 388px; color: var(--white); }
  .brand-lockup__name { font-weight: 700; letter-spacing: -1px; line-height: 1; }
  .brand-lockup--light .brand-lockup__name { font-size: 42px; }
  .brand-lockup__divider { width: 1px; align-self: stretch; margin: 0 12px; }
  .brand-lockup--light .brand-lockup__divider { background: rgba(255,255,255,0.7); height: 46px; }
  .brand-lockup__title { font-weight: 700; line-height: 1.1; }
  .brand-lockup--light .brand-lockup__title { font-size: 14px; }
  .brand-lockup__subtitle { font-weight: 600; letter-spacing: 1.6px; }

  /* back */
  .brand-lockup--color { left: 176px; top: 40px; color: var(--ink); }
  .brand-lockup--color .brand-lockup__name { font-size: 66px; color: var(--red); letter-spacing: -2px; }
  .brand-lockup--color .brand-lockup__divider { background: #d8d8d8; height: 80px; margin: 0 22px; }
  .brand-lockup--color .brand-lockup__title { font-size: 23px; color: var(--black); }
  .brand-lockup--color .brand-lockup__subtitle { font-size: 21px; letter-spacing: 2.4px; }
  .mission {
    position: absolute; left: 0; right: 0; top: 134px;
    text-align: center; color: var(--black);
  }
  .mission__lead { font-size: 21px; line-height: 26px; }
  .mission__pillars { font-size: 20px; line-height: 26px; letter-spacing: 0.6px; }
  .appeal {
    position: absolute; left: 22px; top: 211px; width: 488px; height: 101px;
    background: var(--yellow);
    padding: 12px 14px; font-size: 20px; line-height: 25px; color: var(--black);
    box-shadow: 0 10px 14px -8px rgba(0,0,0,0.25);
  }
  .appeal__lead { color: var(--red); font-weight: 700; }
  .contact {
    position: absolute; left: 576px; top: 210px;
    border-left: 2px solid var(--orange); padding-left: 8px;
    font-size: 19px; line-height: 25px; color: var(--black);
  }
  .contact__intro { margin-bottom: 6px; }
  .pledge-band {
    position: absolute; left: 0; right: 0; top: 356px; bottom: 0;
    background: var(--band-yellow);
  }
  .pledge-box {
    position: absolute; left: 62px; top: 342px; width: 94px; height: 94px;
    border: 3px solid var(--black); background: var(--white);
  }
  .pledge-text {
    position: absolute; left: 200px; top: 367px; width: 580px;
    text-align: center; font-weight: 700; font-size: 18px; line-height: 24px; color: var(--black);
  }
  .partners {
    position: absolute; left: 770px; top: 345px; width: 232px; height: 93px;
    background: var(--white); text-align: center; padding-top: 8px;
  }
  .partners__label { font-size: 17px; color: var(--black); }
  .partners__badges { display: flex; justify-content: space-around; margin-top: 10px; padding: 0 22px; }
  .partner-badge { width: 30px; height: 30px; }
  .partner-badge--one { background: #8a6d1f; border-radius: 4px; }
  .partner-badge--two { background: #1f8ed0; border-radius: 50%; }
</style>
</head>
<body>
  <section class="slip slip--front">
    <div class="hero-photo" role="img" aria-label="Photo of cupped hands holding dark soil with a young green seedling, soft blue-grey background"></div>
    <div class="accent-rule accent-rule--top"></div>
    <div class="accent-rule accent-rule--bottom"></div>
    <p class="quote">Modern medical advances have helped millions of people live longer, healthier lives. We owe these improvements to decades of investment in medical research.</p>
    <p class="quote__author">-Ira Delmont</p>
    <div class="brand-lockup brand-lockup--light">
      <span class="brand-lockup__name">PLIVET</span>
      <span class="brand-lockup__divider"></span>
      <div class="brand-lockup__title">Westmere Study Group<br><span class="brand-lockup__subtitle">for Joint &amp; Muscle Health</span></div>
    </div>
  </section>

  <section class="slip slip--back">
    <div class="brand-lockup brand-lockup--color">
      <span class="brand-lockup__name">PLIVET</span>
      <span class="brand-lockup__divider"></span>
      <div class="brand-lockup__title">Westmere Study Group<br><span class="brand-lockup__subtitle">for Joint &amp; Muscle Health</span></div>
    </div>
    <div class="mission">
      <p class="mission__lead">We are passionate Clinicians and Educators focused on</p>
      <p class="mission__pillars">EMPOWERING PATIENTS &nbsp;·&nbsp; ADVANCING RESEARCH &nbsp;·&nbsp; IMPROVING CLINICAL CARE</p>
    </div>
    <div class="appeal"><span class="appeal__lead">We need your help!</span> Donations help run the PLIVET research program and without your support, it simply wouldn’t be possible.</div>
    <div class="contact">
      <p class="contact__intro">To learn more, talk to your surgeon or<br>contact us:</p>
      <p>Phone: 555-014-2290</p>
      <p>Email: research@westmerestudy.example</p>
    </div>
    <div class="pledge-band"></div>
    <div class="pledge-box"></div>
    <p class="pledge-text">YES, I would like to help! Visit the following link:<br>https://giving.norvalenu.example/medicine/PLIVET</p>
    <div class="partners">
      <p class="partners__label">In partnership with:</p>
      <div class="partners__badges">
        <span class="partner-badge partner-badge--one"></span>
        <span class="partner-badge partner-badge--two"></span>
      </div>
    </div>
  </section>
</body>
</html>
```